36" inch (height) x 96" inch (width) Banner for Baseball Field

Hello. This project is an advertisement that will be printed onto a 3 foot by 8 foot full color banner and placed at little league fields in Southern California. A theme of the banner can be baseball. The company is my law office practicing Estate Planning and Tax Law. I am uploading the current business card, which has the logo, website, and telephone number. You can also pull images from www.rkpembrove.com I would like the banner to be a fun design that incorporates baseball somehow, but draws attention to my law and tax office, and my website. Please be creative, and have fun with it. The colors of my practice are included in the logo. At the bottom, it should say "Attorney Advertisement," but this can be in very small font in the bottom right or left corner.

Target Market(s)

Youth Baseball Fans

Industry/Entity Type

Law; Accounting

Colors

Designer to choose colors to be used in the design.

Requirements
Must have
• My telephone number. My website.
Nice to have
• Would like to see "Estate Planning" and "Tax Law and Preparation" Would also like to see "Attorney" and "CPA" or "Certified Public Accountant" prominently diplayed

```html
<!DOCTYPE html>
<html lang="en">
<head>
<meta charset="utf-8">
<title>RK Pembrove – Ballfield Banner</title>
<link rel="stylesheet" href="https://fonts.googleapis.com/css2?family=Open+Sans:wght@600;700&family=Poppins:wght@500;600;700&family=PT+Sans:wght@400&display=swap">
<style>
  :root {
    --canvas: #9a9a9a;
    --white: #ffffff;
    --brand-blue: #1a8cf0;
    --logo-blue: #1e8fd6;
    --ink: #141414;
    --sky-top: #1d3f66;
    --sky-mid: #8fbde0;
    --stands: #1b1b24;
    --field: #2f7a2a;
  }
  * { margin: 0; padding: 0; box-sizing: border-box; }
  html, body { width: 1200px; height: 1200px; overflow: hidden; background: var(--canvas); }
  .banner {
    position: absolute; left: 92px; top: 114px;
    width: 1016px; height: 381px;
  }
  .banner-shapes { position: absolute; inset: 0; }
  .brand {
    position: absolute; left: 0; top: 40px; width: 244px;
    display: flex; flex-direction: column; align-items: center;
  }
  .brand-mark {
    width: 62px; height: 62px; border-radius: 50%;
    border: 4px solid var(--logo-blue);
  }
  .brand-name {
    margin-top: 20px;
    font-family: "Poppins", sans-serif; font-weight: 500;
    font-size: 22px; letter-spacing: 1px; color: var(--logo-blue);
  }
  .address {
    position: absolute; left: 0; top: 176px; width: 244px;
    font-family: "Poppins", sans-serif; font-weight: 600;
    font-size: 17.5px; line-height: 23.5px; letter-spacing: 1.6px;
    color: var(--ink); text-align: center; font-style: normal;
  }
  .headline {
    position: absolute; left: 352px; top: 22px;
    font-family: "Open Sans", sans-serif; font-weight: 700;
    font-size: 58px; letter-spacing: -1.5px; color: var(--white);
    line-height: 1;
  }
  .credentials {
    position: absolute; left: 352px; top: 88px;
    font-family: "Poppins", sans-serif; font-weight: 700;
    font-size: 29px; letter-spacing: 3px; color: var(--ink); line-height: 1;
  }
  .contact-web {
    position: absolute; left: 352px; top: 250px;
    font-family: "PT Sans", sans-serif; font-weight: 400;
    font-size: 26px; color: var(--white); line-height: 1;
  }
  .phones {
    position: absolute; left: 0; right: 0; top: 301px; height: 80px;
    display: flex; align-items: center; justify-content: center;
    font-family: "Poppins", sans-serif; font-weight: 700;
    font-size: 47px; letter-spacing: 4px; color: var(--white);
  }
</style>
</head>
<body>
  <section class="banner">
    <svg class="banner-shapes" width="1016" height="381" viewBox="0 0 1016 381">
      <defs>
        <linearGradient id="stadium-sky" x1="0" y1="0" x2="0" y2="1">
          <stop offset="0" stop-color="var(--sky-top)"/>
          <stop offset="0.4" stop-color="var(--sky-mid)"/>
          <stop offset="0.72" stop-color="#2b3442"/>
          <stop offset="0.82" stop-color="var(--field)"/>
          <stop offset="1" stop-color="#245f22"/>
        </linearGradient>
        <linearGradient id="stadium-stands" x1="0" y1="0" x2="1" y2="0">
          <stop offset="0" stop-color="var(--stands)" stop-opacity="0"/>
          <stop offset="0.55" stop-color="var(--stands)" stop-opacity="0.55"/>
          <stop offset="1" stop-color="var(--stands)" stop-opacity="0.9"/>
        </linearGradient>
      </defs>
      <rect class="panel-white" x="0" y="0" width="1016" height="301" fill="var(--white)"/>
      <g role="img" aria-label="Photo of a floodlit baseball stadium with stands and a green field under a blue sky">
        <polygon points="225,0 1016,0 1016,293 267,293" fill="url(#stadium-sky)"/>
        <polygon points="225,0 1016,0 1016,293 267,293" fill="url(#stadium-stands)"/>
      </g>
      <polygon class="accent-stripe" points="217,0 226,0 268,301 259,301" fill="var(--brand-blue)"/>
      <rect class="phone-band" x="0" y="301" width="1016" height="80" fill="var(--brand-blue)"/>
    </svg>

    <div class="brand">
      <div class="brand-mark"></div>
      <div class="brand-name">RK PEMBROVE</div>
    </div>

    <address class="address">
      284 Harlow Street<br>
      Penthouse Suite 318<br>
      Cedar Vale,<br>
      California&nbsp; 90000
    </address>

    <h1 class="headline">Raymond K. Pembrove</h1>
    <p class="credentials">Attorney &amp; CPA</p>
    <p class="contact-web">ray@rkpembrove.com / www.rkpembrove.com</p>

    <p class="phones">(555) 014-2237 / (555) 018-0462</p>
  </section>
</body>
</html>
```